Saltwater In store poster design

We need a poster design that will be hung in aquarium stores, to advertise that they use our natural saltwater.

Must use logo as well as be bright and colourful. We are trying to communicate that the water is natural (so good for your marine tank) as well as clean and safe, so please consider this in your design.

Must say something along the lines of "We use natural ocean water supplied by Reef Bucket in our store" as well as "you can purchase natural ocean water here"

Open to all design types and suggestions as we will update the brief if we find one specific style that we prefer.

Target Market(s)

Customers who own marine aquariums

Industry/Entity Type

Store

Requirements
Must have
• Reef bucket logo (does not need to have blue background attached, just the oval)

Be eye catching

Have similar phrases to those above

```html
<!DOCTYPE html>
<html lang="en">
<head>
<meta charset="UTF-8">
<title>Natural Ocean Water – In-Store Poster</title>
<link rel="stylesheet" href="https://fonts.googleapis.com/css2?family=Arvo:wght@700&display=swap">
<style>
  :root {
    --backdrop: #e4e5e7;
    --poster-black: #000000;
    --ocean-light: #5fb6e6;
    --ocean-mid: #1f6fb8;
    --sky-top: #1c4fa0;
    --sky-glow: #f2b15a;
    --reef-purple: #4a3a78;
    --white: #ffffff;
  }
  * { margin: 0; padding: 0; box-sizing: border-box; }
  html, body {
    width: 1200px;
    height: 900px;
    overflow: hidden;
    background: var(--backdrop);
  }
  .poster {
    position: absolute;
    left: 300px;
    top: 26px;
    width: 600px;
    height: 848px;
    background: var(--poster-black);
    overflow: hidden;
    font-family: "Arvo", "Rockwell", serif;
    color: var(--white);
  }
  .hero-photo {
    position: absolute;
    left: 0; top: 0;
    width: 600px;
    height: 486px;
    background:
      linear-gradient(180deg,
        var(--sky-top) 0%,
        #4f7fc0 18%,
        var(--sky-glow) 33%,
        #2c3f66 40%,
        #1a5fb0 44%,
        var(--ocean-mid) 58%,
        #174f95 74%,
        var(--reef-purple) 88%,
        #1b2340 100%);
  }
  .headline {
    position: absolute;
    left: 0;
    width: 600px;
    text-align: center;
    font-weight: 700;
    line-height: 1;
    white-space: nowrap;
  }
  .headline-top {
    top: 528px;
    font-size: 69px;
    color: var(--white);
  }
  .headline-main {
    top: 600px;
    font-size: 67px;
    letter-spacing: 1px;
    text-transform: uppercase;
    background: linear-gradient(180deg, var(--white) 0%, var(--white) 55%, var(--ocean-light) 55%, var(--ocean-light) 100%);
    -webkit-background-clip: text;
    background-clip: text;
    color: transparent;
  }
  .supplier-line {
    position: absolute;
    left: 0;
    top: 704px;
    width: 600px;
    display: flex;
    justify-content: center;
    align-items: center;
    gap: 14px;
    font-size: 27px;
    font-weight: 700;
    line-height: 1;
    white-space: nowrap;
    color: var(--ocean-light);
  }
  .supplier-name {
    color: var(--white);
  }
  .footer-band {
    position: absolute;
    left: 0; top: 786px;
    width: 600px;
    height: 62px;
  }
  .footer-text {
    position: absolute;
    left: 0;
    top: 812px;
    width: 600px;
    text-align: center;
    font-size: 23px;
    font-weight: 700;
    line-height: 1;
    white-space: nowrap;
    color: var(--white);
  }
</style>
</head>
<body>
  <main class="poster">
    <div class="hero-photo" role="img" aria-label="Photo of a colourful reef aquarium with corals and tropical fish beneath a sunset sky, water surface wave across the middle"></div>

    <h1 class="headline headline-top">we use natural</h1>
    <h2 class="headline headline-main">Ocean Water</h2>

    <p class="supplier-line">
      <span>supplied by</span>
      <span class="supplier-name">Reef Bucket</span>
      <span>in our store</span>
    </p>

    <svg class="footer-band" viewBox="0 0 600 62" preserveAspectRatio="none" aria-hidden="true">
      <path d="M0 12 C120 0 200 22 320 14 C430 6 520 2 600 10 L600 62 L0 62 Z" fill="var(--ocean-light)"/>
    </svg>
    <p class="footer-text">you can purchase natural ocean water here</p>
  </main>
</body>
</html>
```